POOL BUILDING CONTRACTOR

our company has shifter focus over the past 18 month we no longer have a retail store and no longer clean pools we build concrete pools. our website if 5 years old we need a completely new site that shows our core product, building concrete pools & renovate concrete pools

here is a few of our competitors;
brantelwaters.com
okvimbuilders.com
ridgeviewlagoonworks.com
plunvora.com
halvertonbasinsandtubs.com
dremblewaterne.com

one we land on a final design I will upload customer before and after photos and any other content needed

Target Market(s)

People looking to build or renovate there pool

Industry/Entity Type

swimming pool

Coding

Coded - Design and coding required

Number of Pages Required

5+ page

Colors
0054AA
0677BA
7BADD7
CADEEF
E8F1F8

Requirements
Must have
• financing Service-Repairs & liners new build-photos renovate-remodeling design-consult customer-reviews Gallery Before-After Contact us 3D Design & Modeling construction process & Timeline Equipment Features Hardscapes I like these sites https://meadowlarkbasinsbycraft.com/ https://holtbergwaters.com/

```html
<!DOCTYPE html>
<html lang="en">
<head>
<meta charset="utf-8">
<title>Aquelle – Leading Luxury Pools Builder</title>
<link href="https://fonts.googleapis.com/css2?family=Poppins:ital,wght@0,400;0,500;0,600;0,700;1,400&display=swap" rel="stylesheet">
<style>
:root{
  --blue-deep:#0054AA;
  --blue:#0677BA;
  --blue-soft:#7BADD7;
  --blue-pale:#CADEEF;
  --blue-mist:#E8F1F8;
  --ink:#333a44;
  --muted:#5a6270;
  --white:#ffffff;
  --page:#fbfcfe;
}
*{box-sizing:border-box;margin:0;padding:0}
html,body{width:1200px;height:3985px;overflow:hidden}
body{position:relative;background:var(--page);font-family:'Poppins',sans-serif;color:var(--ink)}
.abs{position:absolute}
.photo{position:absolute;border-radius:2px}
.btn{position:absolute;display:flex;align-items:center;justify-content:center;font-size:11px;font-weight:600;text-transform:uppercase;letter-spacing:.2px;border-radius:4px;text-decoration:none}
.btn-blue{background:var(--blue-deep);color:var(--white)}
.btn-light{background:#2f8dc8;color:var(--white)}
.btn-white{background:var(--white);color:var(--blue-deep)}

/* header */
.site-header{position:absolute;left:0;top:0;width:1200px;height:88px;background:var(--white)}
.brand{position:absolute;display:flex;align-items:center;gap:8px;font-weight:700;color:var(--blue-deep)}
.brand-mark{background:var(--blue);border-radius:4px}
.main-nav a{position:absolute;top:32px;font-size:17px;color:var(--blue-deep);text-decoration:none;font-weight:500}
.main-nav a.active{border-bottom:3px solid var(--blue-deep);padding-bottom:6px}
.social{position:absolute;border-radius:50%;background:var(--blue-deep)}

/* hero */
.hero{position:absolute;left:0;top:88px;width:1200px;height:668px;
  background:linear-gradient(180deg,#c9b89a 0%,#9a8d78 22%,#4d7e8c 42%,#2f6f82 60%,#5b8f98 78%,#8ea9a6 100%)}
.hero-title{position:absolute;left:198px;top:220px;font-size:74px;line-height:94px;font-weight:600;color:var(--white);white-space:nowrap}
.hero-text{position:absolute;left:198px;top:432px;font-size:13.5px;line-height:22px;font-weight:500;color:var(--white);white-space:nowrap}
.phone-tab{position:absolute;left:761px;top:88px;width:318px;height:59px;background:var(--blue-deep);border-radius:0 0 8px 8px;color:var(--white);font-weight:600;font-size:21px;display:flex;align-items:center;justify-content:center;gap:10px}

/* section headings */
.section-title{position:absolute;left:0;width:1200px;text-align:center;font-weight:600;color:var(--blue-deep);font-size:48px;line-height:51px}
.section-lead{position:absolute;left:0;width:1200px;text-align:center;font-size:14px;line-height:22px;font-weight:500}

/* service cards */
.service-card{position:absolute;width:302px;height:341px;border:1.5px solid var(--blue-soft);border-radius:12px;background:var(--white)}
.service-card .photo{left:29px;top:30px;width:244px;height:182px}
.service-card h3{position:absolute;left:29px;top:234px;font-size:21px;font-weight:500;color:var(--blue)}
.service-card p{position:absolute;left:29px;top:271px;width:250px;font-size:13.5px;line-height:21px;font-weight:500}

.team-panel{position:absolute;left:448px;top:1388px;width:631px;height:333px;border-radius:12px;background:linear-gradient(160deg,var(--blue-deep),var(--blue))}
.team-panel h2{position:absolute;left:34px;top:56px;font-size:44px;font-weight:600;color:var(--white);white-space:nowrap}
.team-panel p{position:absolute;left:34px;top:138px;font-size:13.5px;line-height:21.5px;font-weight:500;color:var(--white);white-space:nowrap}

/* residential */
.res-title{position:absolute;left:634px;top:1880px;font-size:48px;line-height:52px;font-weight:600;color:var(--blue-deep)}
.res-text{position:absolute;left:634px;top:2007px;font-size:13.5px;line-height:22px;color:var(--muted);white-space:nowrap}
.checks{position:absolute;left:634px;top:2104px;list-style:none}
.checks li{display:flex;align-items:center;gap:8px;height:31px;font-size:13.5px;color:var(--muted)}

/* testimonials */
.quote-card{position:absolute;top:2945px;width:255px;height:88px;background:var(--blue-mist);border-radius:6px;padding:16px 18px;font-size:12.5px;line-height:19.5px;font-style:italic;color:#555d68}
.reviewer{position:absolute;top:3057px;display:flex;align-items:center;gap:16px;font-size:12px;font-weight:500}
.reviewer .avatar{width:40px;height:40px;border-radius:50%;background:linear-gradient(160deg,var(--blue-soft),var(--blue))}
.dot{position:absolute;top:3134px;width:8px;height:8px;border-radius:50%;background:var(--blue-pale)}
.dot.on{background:var(--blue-deep)}

/* cta */
.cta-panel{position:absolute;left:119px;top:3246px;width:960px;height:321px;border-radius:16px;background:linear-gradient(150deg,var(--blue-deep),var(--blue))}
.cta-panel h2{position:absolute;left:0;top:40px;width:960px;text-align:center;font-size:42px;line-height:52px;font-weight:600;color:var(--white)}
.cta-panel p{position:absolute;left:0;top:165px;width:960px;text-align:center;font-size:14px;line-height:22px;color:var(--white)}

/* footer */
.site-footer{position:absolute;left:0;top:3652px;width:1200px;height:333px;background:linear-gradient(180deg,#eef3f7,#f5f8fa 50%,#e9f1f6)}
.footer-links a{position:absolute;font-size:13.5px;font-weight:500;color:var(--blue-deep);text-decoration:none}
.footer-text{position:absolute;left:128px;top:151px;font-size:13.5px;line-height:22px;color:var(--muted);white-space:nowrap}
</style>
</head>
<body>

<header class="site-header">
  <div class="brand" style="left:128px;top:26px;font-size:28px">
    <span class="brand-mark" style="width:32px;height:32px"></span>Aquelle
  </div>
  <nav class="main-nav">
    <a href="#" class="active" style="left:373px">Home</a>
    <a href="#" style="left:462px">About</a>
    <a href="#" style="left:551px">Services</a>
    <a href="#" style="left:659px">Gallery</a>
    <a href="#" style="left:757px">Contact</a>
  </nav>
  <span class="social" style="left:954px;top:32px;width:24px;height:24px" aria-label="Social profile"></span>
  <span class="social" style="left:988px;top:32px;width:24px;height:24px" aria-label="Social profile"></span>
  <span class="social" style="left:1022px;top:32px;width:24px;height:24px" aria-label="Social profile"></span>
</header>

<section class="hero" role="img" aria-label="Luxury villa with a long infinity swimming pool and terrace loungers"></section>
<div class="phone-tab">
  <svg width="20" height="20" viewBox="0 0 24 24"><path fill="#fff" d="M6.6 10.8a15.1 15.1 0 0 0 6.6 6.6l2.2-2.2c.3-.3.7-.4 1-.2 1.1.4 2.3.6 3.6.6.6 0 1 .4 1 1V20c0 .6-.4 1-1 1C10.6 21 3 13.4 3 4c0-.6.4-1 1-1h3.5c.6 0 1 .4 1 1 0 1.3.2 2.5.6 3.6.1.3 0 .7-.2 1z"/></svg>
  +8 (495) 310 47 62
</div>
<h1 class="hero-title">Leading Luxury<br>Pools Builder</h1>
<p class="hero-text">In tortor ipsum, facilisis quis quam eu, posuere vulputate lorem. Suspendisse faucibus<br>nisi vel velit commodo, vel bibendum erat blandit. Nulla sit amet neque<br>varius imperdiet purus consequat, dapibus</p>
<a class="btn btn-blue" style="left:196px;top:541px;width:208px;height:45px">Get a free quote</a>

<h2 class="section-title" style="top:832px">Why will you choose<br>our services?</h2>
<p class="section-lead" style="top:951px">Vestibulum sagittis felis quis arcu elementum pellentesque. Cras eget odio vulputate, blandit dolor,<br>posuere libero. Nulla commodo felis a eleifend facilisis</p>

<article class="service-card" style="left:128px;top:1037px">
  <div class="photo" role="img" aria-label="Backyard pool beside a stone house and pergola" style="background:linear-gradient(180deg,#b9d3e8 0%,#8c8a7c 45%,#3fb7d8 75%,#cfd2cf 100%)"></div>
  <h3>Pool Building</h3>
  <p>Suspendisse in nunc risus. Nam scelerisque dui eget lacus molestie</p>
</article>
<article class="service-card" style="left:448px;top:1037px">
  <div class="photo" role="img" aria-label="Workers resurfacing an empty pool" style="background:linear-gradient(135deg,#6f6e6a 0%,#8fb9d6 40%,#5aa4d6 100%)"></div>
  <h3>Pool Renovation</h3>
  <p>Etiam venenatis diam id velit vestibulum ultrices</p>
</article>
<article class="service-card" style="left:768px;top:1037px">
  <div class="photo" role="img" aria-label="Round stone spa with custom features" style="background:linear-gradient(180deg,#a8c8e2 0%,#8c7d6c 40%,#6f8e94 70%,#9c9a94 100%)"></div>
  <h3>Custom Features</h3>
  <p>Fusce volutpat aliquet velit, ut interdum quam. Suspendisse</p>
</article>
<article class="service-card" style="left:128px;top:1396px">
  <div class="photo" role="img" aria-label="Pool with raised spa and wooden fence" style="background:linear-gradient(180deg,#7a5a44 0%,#5e4a3d 30%,#2a9cc0 65%,#9b8d7b 100%)"></div>
  <h3>Kitchen Clean</h3>
  <p>Etiam et nisl non nulla faucibus egestas interdum lobortis</p>
</article>

<section class="team-panel">
  <h2>We have a expert team</h2>
  <p>Our specially trained staff will sit down with you to plan your vision &amp; guide you<br>through the design phases, draft and engineer your plans, coordinate city<br>permitting, and manage the swimming pool construction process as well as any<br>other phase to get you in your new Pool</p>
  <a class="btn btn-light" style="left:34px;top:238px;width:216px;height:45px">Get a free quote</a>
</section>

<div class="photo" role="img" aria-label="Bright blue pool with wooden deck and cabana" style="left:128px;top:1855px;width:223px;height:337px;border-radius:12px;background:linear-gradient(180deg,#7fb2e0 0%,#c8dbe8 30%,#7a5c44 45%,#3fc4e2 70%,#8a6a50 100%)"></div>
<div class="photo" role="img" aria-label="House and pool under a cloudy sky" style="left:368px;top:1855px;width:127px;height:84px;border-radius:8px;background:linear-gradient(180deg,#b9d3e8,#8a8779 60%,#4bb6d6)"></div>
<div class="photo" role="img" aria-label="Stone spa in front of a brick house" style="left:368px;top:1957px;width:223px;height:337px;border-radius:12px;background:linear-gradient(180deg,#6fa6dc 0%,#c4d8e6 30%,#8a7464 50%,#7a8f92 75%,#9a9088 100%)"></div>
<div class="photo" role="img" aria-label="Close view of curved pool edge" style="left:224px;top:2209px;width:127px;height:85px;border-radius:8px;background:linear-gradient(180deg,#3aa8e0,#7cc6ec)"></div>

<h2 class="res-title">Residential &amp;<br>Commerical</h2>
<p class="res-text">Mauris ac felis at quam gravida consequat id nec enim. Praesent<br>venenatis lorem quis est convallis, eu cursus ipsum vestibulum.<br>Vivamus sed semper leo</p>
<ul class="checks">
  <li><svg width="13" height="13" viewBox="0 0 14 14"><circle cx="7" cy="7" r="6" fill="none" stroke="var(--blue)" stroke-width="1.4"/><path d="M4 7.2l2 2 4-4" fill="none" stroke="var(--blue)" stroke-width="1.4"/></svg>Duis rhoncus nisi augue, elementum consectetur odio</li>
  <li><svg width="13" height="13" viewBox="0 0 14 14"><circle cx="7" cy="7" r="6" fill="none" stroke="var(--blue)" stroke-width="1.4"/><path d="M4 7.2l2 2 4-4" fill="none" stroke="var(--blue)" stroke-width="1.4"/></svg>Maecenas hendrerit arcu eget est</li>
  <li><svg width="13" height="13" viewBox="0 0 14 14"><circle cx="7" cy="7" r="6" fill="none" stroke="var(--blue)" stroke-width="1.4"/><path d="M4 7.2l2 2 4-4" fill="none" stroke="var(--blue)" stroke-width="1.4"/></svg>Proin quis lorem non sem rutrum tempus</li>
</ul>
<a class="btn btn-blue" style="left:634px;top:2222px;width:252px;height:45px">View recent projects</a>

<h2 class="section-title" style="top:2395px">Recent Work</h2>
<div class="photo" role="img" aria-label="Pool with red loungers and palm trees" style="left:128px;top:2481px;width:271px;height:152px;background:linear-gradient(180deg,#7fb2e0,#cfdbe4 40%,#3fb7d8 70%,#7a5c44)"></div>
<div class="photo" role="img" aria-label="Freeform pool surrounded by garden" style="left:408px;top:2481px;width:432px;height:152px;background:linear-gradient(180deg,#3f7a3a,#2fa6e0 40%,#5cc0ec 70%,#c9b79e)"></div>
<div class="photo" role="img" aria-label="Workers finishing an empty pool" style="left:849px;top:2481px;width:222px;height:152px;background:linear-gradient(135deg,#6f6e6a,#8fb9d6 45%,#5aa4d6)"></div>
<div class="photo" role="img" aria-label="Round stone spa beside a house" style="left:128px;top:2642px;width:276px;height:183px;background:linear-gradient(180deg,#a8c8e2,#8c7d6c 45%,#6f8e94 75%,#9c9a94)"></div>
<div class="photo" role="img" aria-label="Pool and raised spa with wooden fence" style="left:411px;top:2642px;width:326px;height:183px;background:linear-gradient(180deg,#7a5a44,#5e4a3d 30%,#2a9cc0 65%,#9b8d7b)"></div>
<div class="photo" role="img" aria-label="Backyard pool by a stone house" style="left:745px;top:2642px;width:326px;height:183px;background:linear-gradient(180deg,#b9d3e8,#8c8a7c 45%,#3fb7d8 80%,#cfd2cf)"></div>

<blockquote class="quote-card" style="left:167px">Morbi finibus, tortor a suscipit faucibus, felis magna ornare nunc, in tristique nisl sem rutru</blockquote>
<blockquote class="quote-card" style="left:472px">Nunc dictum facilisis turpis et mollis. Duis eget metus a lorem placerat dignissim sed nec risus</blockquote>
<blockquote class="quote-card" style="left:776px">Morbi finibus, tortor a suscipit faucibus, felis magna ornare nunc, in tristique nisl sem rutru</blockquote>
<div class="reviewer" style="left:184px"><span class="avatar" role="img" aria-label="Customer portrait"></span>Lena Dorvik</div>
<div class="reviewer" style="left:489px"><span class="avatar" role="img" aria-label="Customer portrait"></span>Mira Hallan</div>
<div class="reviewer" style="left:793px"><span class="avatar" role="img" aria-label="Customer portrait"></span>Mira Hallan</div>
<span class="dot" style="left:568px"></span>
<span class="dot" style="left:587px"></span>
<span class="dot" style="left:605px"></span>
<span class="dot on" style="left:624px"></span>

<section class="cta-panel">
  <h2>Leading Luxury<br>Pools Builder</h2>
  <p>Quisque imperdiet mauris nec faucibus vestibulum. Ut vestibulum est ac<br>hendrerit pharetra. Integer sit amet laoreet lectus</p>
  <a class="btn btn-white" style="left:373px;top:236px;width:215px;height:44px">Get a quote now</a>
</section>

<footer class="site-footer" role="img" aria-label="Faint view of a poolside terrace">
  <div class="brand" style="left:138px;top:66px;font-size:36px">
    <span class="brand-mark" style="width:44px;height:44px"></span>Aquelle
  </div>
  <p class="footer-text">Etiam et nisl non nulla faucibus<br>egestas interdum lobortis odio</p>
  <nav class="footer-links">
    <a href="#" style="left:368px;top:72px">Home</a>
    <a href="#" style="left:368px;top:111px">About</a>
    <a href="#" style="left:368px;top:150px">Services</a>
    <a href="#" style="left:368px;top:189px">Gallery</a>
    <a href="#" style="left:368px;top:228px">Contact</a>
    <a href="#" style="left:608px;top:72px">Home</a>
    <a href="#" style="left:608px;top:111px">About</a>
    <a href="#" style="left:608px;top:150px">Services</a>
    <a href="#" style="left:608px;top:189px">Gallery</a>
    <a href="#" style="left:608px;top:228px">Contact</a>
  </nav>
  <span class="social" style="left:849px;top:62px;width:33px;height:33px" aria-label="Social profile"></span>
  <span class="social" style="left:891px;top:62px;width:33px;height:33px" aria-label="Social profile"></span>
  <span class="social" style="left:933px;top:62px;width:33px;height:33px" aria-label="Social profile"></span>
</footer>

</body>
</html>
```